Holzkitt Label

Need a product label for a water-based wood putty.
The logo will be inserted by us.
The product is designed to appeal to professional users such as carpenters.

```html
<!DOCTYPE html>
<html lang="en">
<head>
<meta charset="utf-8">
<title>Holzkitt Label</title>
<link rel="stylesheet" href="https://fonts.googleapis.com/css2?family=Permanent+Marker&family=Open+Sans:wght@700&family=Luckiest+Guy&display=swap">
<style>
  :root {
    --backdrop: #22435f;
    --label-blue: #1a9fc4;
    --label-white: #f4f4f2;
    --orange-light: #eb9a22;
    --orange-mid: #e8721f;
    --orange-deep: #d63b17;
    --ink: #141414;
    --photo-plaster: #8d969c;
    --photo-plaster-dark: #5a6a80;
    --photo-wood: #7a4a3c;
    --photo-wood-dark: #3e2621;
  }
  * { margin: 0; padding: 0; box-sizing: border-box; }
  html, body { width: 1200px; height: 1198px; overflow: hidden; }
  body { background: var(--backdrop); position: relative; }

  .label {
    position: absolute;
    left: 150px;
    top: 239px;
    width: 900px;
    height: 720px;
    overflow: hidden;
  }
  .label-art { position: absolute; inset: 0; width: 100%; height: 100%; display: block; }

  .tagline {
    position: absolute;
    left: 28px;
    top: 128px;
    font-family: "Luckiest Guy", "Arial Black", sans-serif;
    font-size: 38px;
    line-height: 1;
    letter-spacing: 1px;
    color: var(--label-white);
    transform: rotate(-17deg);
    transform-origin: left bottom;
    white-space: nowrap;
  }
  .product-name {
    position: absolute;
    left: 280px;
    width: 500px;
    top: 155px;
    text-align: center;
    font-family: "Permanent Marker", "Impact", sans-serif;
    font-weight: 400;
    font-size: 112px;
    line-height: 1;
    letter-spacing: 3px;
    color: var(--ink);
    white-space: nowrap;
  }
  .product-name, .product-type { display: flex; justify-content: center; }
  .product-type {
    position: absolute;
    left: 280px;
    width: 500px;
    top: 285px;
    font-family: "Open Sans", Arial, sans-serif;
    font-weight: 700;
    font-size: 30px;
    line-height: 1.2;
    color: var(--ink);
    white-space: nowrap;
  }
</style>
</head>
<body>
  <main class="label">
    <svg class="label-art" viewBox="0 0 900 720" xmlns="http://www.w3.org/2000/svg">
      <defs>
        <linearGradient id="orange-band" x1="0" y1="0" x2="1" y2="0">
          <stop offset="0" stop-color="var(--orange-light)"/>
          <stop offset="0.5" stop-color="var(--orange-mid)"/>
          <stop offset="1" stop-color="var(--orange-deep)"/>
        </linearGradient>
        <linearGradient id="plaster-photo" x1="0" y1="0" x2="1" y2="1">
          <stop offset="0" stop-color="var(--photo-plaster-dark)"/>
          <stop offset="1" stop-color="var(--photo-plaster)"/>
        </linearGradient>
        <linearGradient id="wood-photo" x1="0" y1="0" x2="1" y2="0">
          <stop offset="0" stop-color="var(--photo-wood)"/>
          <stop offset="1" stop-color="var(--photo-wood-dark)"/>
        </linearGradient>
      </defs>

      <rect class="label-ground" width="900" height="720" fill="var(--label-blue)"/>

      <g class="photo-strip">
        <rect role="img" aria-label="Photo of a worker's hand smoothing putty onto a wall with a spatula"
              x="0" y="300" width="900" height="420" fill="url(#plaster-photo)"/>
        <path role="img" aria-label="Photo of a gloved hand painting a vertical wooden board fence with a roller"
              d="M505 340 L900 300 L900 720 L210 720 C275 600 395 470 505 340 Z" fill="url(#wood-photo)"/>
        <path class="photo-divider" d="M170 720 C240 600 360 470 470 340 L505 340 C395 470 275 600 210 720 Z" fill="var(--label-white)"/>
      </g>

      <path class="swoosh-edge" d="M0 180 C250 100 600 70 900 20 L900 352 C700 372 500 382 300 422 C180 447 80 462 0 472 Z" fill="var(--label-white)"/>
      <path class="swoosh" d="M0 200 C250 120 600 90 900 40 L900 330 C700 350 500 360 300 400 C180 425 80 440 0 450 Z" fill="url(#orange-band)"/>
    </svg>

    <p class="tagline">100 % SECURITY</p>
    <h1 class="product-name">HOLZKITT</h1>
    <p class="product-type">Water-based wood putty</p>
  </main>
</body>
</html>
```